New Business Cards for KM&DR

We need updated business cards for a staff of 15 engineers, estimators, project managers, and sales people. We have recently begun changes to our website and marketing material to improve our look and branding. We are an established fabricator specializing in pressure vessels, tanks, and structural steel. The owners require us to use the existing logo and old english text design. Also, we prefer dark grey or mostly black cards.
Target Market(s)
Engineers, purchasing agents, estimators, and project managers of; mining companies, refineries, industrial construction professionals
Industry/Entity Type
Business
Contact Information for Business Card
Logo, phone, website, email, etc.
Look and feel
Each slider illustrates characteristics of the customer's brand and the style your logo design should communicate.

```html
<!DOCTYPE html>
<html lang="en">
<head>
<meta charset="utf-8">
<title>KM&amp;DR Business Card</title>
<link rel="stylesheet" href="https://fonts.googleapis.com/css2?family=Oswald:wght@600&family=Open+Sans:wght@400;700&family=Pirata+One&display=swap">
<style>
  :root {
    --stage: #2b2825;
    --card-black: #0b0b0b;
    --card-deep: #151515;
    --gold-light: #f6e27a;
    --gold: #d9b42c;
    --gold-dark: #8a6a12;
    --ink-light: #d8d8d8;
    --ink-dim: #a9a9a9;
  }
  * { box-sizing: border-box; margin: 0; padding: 0; }
  html, body { width: 1200px; height: 961px; overflow: hidden; }
  body {
    background: var(--stage);
    font-family: "Open Sans", sans-serif;
    position: relative;
  }
  .card {
    position: absolute;
    top: 165px;
    width: 360px;
    height: 630px;
    background: radial-gradient(ellipse at 50% 35%, var(--card-deep), var(--card-black) 75%);
    box-shadow: 0 18px 40px rgba(0,0,0,.55);
    overflow: hidden;
  }
  .card--front { left: 200px; }
  .card--back { left: 640px; }

  /* front */
  .brand-mark {
    position: absolute; top: 150px; left: 0; right: 0;
    display: flex; align-items: center; justify-content: center; gap: 12px;
  }
  .brand-mark__dot {
    width: 22px; height: 22px; border-radius: 50%; background: var(--gold);
  }
  .brand-mark__name {
    font-weight: 700; font-size: 44px; color: var(--gold); letter-spacing: 1px;
  }
  .company-name {
    position: absolute; top: 290px; left: 0; right: 0; text-align: center;
    font-weight: 700; font-size: 40px; color: var(--gold); letter-spacing: 1px;
  }
  .company-tagline {
    position: absolute; top: 360px; left: 0; right: 0; text-align: center;
    font-size: 17px; color: var(--ink-light); letter-spacing: 0.5px;
  }
  .company-initials {
    position: absolute; bottom: 80px; left: 0; right: 0; text-align: center;
    font-size: 22px; font-weight: 700; color: var(--ink-light); letter-spacing: 2px;
  }

  /* back */
  .gold-crest { position: absolute; top: 0; left: 0; width: 360px; height: 150px; }
  .crest-name {
    position: absolute; top: 62px; left: 0; right: 0; text-align: center;
    font-weight: 700; font-size: 18px; color: #2a1e04; letter-spacing: 1px;
  }
  .holder-name {
    position: absolute; top: 185px; left: 0; right: 0; text-align: center;
    font-family: "Oswald", sans-serif; font-weight: 600; font-size: 48px;
    color: var(--gold); letter-spacing: 2px;
  }
  .holder-role {
    position: absolute; top: 255px; left: 0; right: 0; text-align: center;
    font-family: "Pirata One", serif; font-size: 24px; color: var(--gold);
  }
  .gold-rule {
    position: absolute; top: 300px; left: 50px; width: 260px; height: 2px;
    background: linear-gradient(90deg, transparent, var(--gold), transparent);
  }
  .contact-list {
    position: absolute; top: 335px; left: 40px; right: 30px; list-style: none;
  }
  .contact-list li {
    display: flex; align-items: flex-start; gap: 16px;
    color: var(--ink-light); font-size: 16px; line-height: 1.35; margin-bottom: 22px;
  }
  .contact-list .contact-phone { font-size: 24px; }
  .contact-list svg { flex: 0 0 18px; width: 18px; height: 18px; margin-top: 2px; }
</style>
</head>
<body>

<section class="card card--front" aria-label="Card front">
  <div class="brand-mark">
    <span class="brand-mark__dot"></span>
    <span class="brand-mark__name">KM&amp;DR</span>
  </div>
  <div class="company-name">Kestrelmoor</div>
  <div class="company-tagline">Vessel and Tank Fabricators</div>
  <div class="company-initials">KM&amp;DR</div>
</section>

<section class="card card--back" aria-label="Card back">
  <svg class="gold-crest" viewBox="0 0 360 150" aria-hidden="true">
    <defs>
      <linearGradient id="crestGold" x1="0" y1="0" x2="0" y2="1">
        <stop offset="0" stop-color="#f6e27a"/>
        <stop offset="0.55" stop-color="#d9b42c"/>
        <stop offset="1" stop-color="#8a6a12"/>
      </linearGradient>
    </defs>
    <polygon points="50,0 310,0 310,95 270,140 90,140 50,95" fill="url(#crestGold)"/>
    <polygon points="50,95 90,140 270,140 310,95" fill="none" stroke="#f6e27a" stroke-width="2"/>
  </svg>
  <div class="crest-name">KM&amp;DR</div>

  <div class="holder-name">NAME</div>
  <div class="holder-role">Designation</div>
  <div class="gold-rule"></div>

  <ul class="contact-list">
    <li>
      <svg viewBox="0 0 18 18"><path d="M9 1a6 6 0 0 0-6 6c0 4.5 6 10 6 10s6-5.5 6-10a6 6 0 0 0-6-6zm0 8.2A2.2 2.2 0 1 1 9 4.8a2.2 2.2 0 0 1 0 4.4z" fill="#d8d8d8"/></svg>
      <span>418 Ridge Avenue, # 210<br>Millbrook, UT 84000-0210</span>
    </li>
    <li class="contact-phone">
      <svg viewBox="0 0 18 18"><path d="M4 1l3 3-2 2c1 2.5 3 4.5 5.5 5.5l2-2 3 3-2 3C7 17 1 11 1 4z" fill="#d8d8d8"/></svg>
      <span>555.014.2290</span>
    </li>
    <li>
      <svg viewBox="0 0 18 18"><rect x="1" y="3.5" width="16" height="11" fill="none" stroke="#d8d8d8" stroke-width="1.5"/><path d="M1 3.5l8 6 8-6" fill="none" stroke="#d8d8d8" stroke-width="1.5"/></svg>
      <span>sales@kmanddr.com</span>
    </li>
    <li>
      <svg viewBox="0 0 18 18"><circle cx="9" cy="9" r="7.5" fill="none" stroke="#d8d8d8" stroke-width="1.5"/><ellipse cx="9" cy="9" rx="3.2" ry="7.5" fill="none" stroke="#d8d8d8" stroke-width="1.2"/><path d="M1.5 9h15" stroke="#d8d8d8" stroke-width="1.2"/></svg>
      <span>www.kmanddr.com</span>
    </li>
  </ul>
</section>

</body>
</html>
```